Yummy Mummy Flyer

Flyer that will be handed and also appear in magazine advertisements.

The campaign is aimed women that want to get pregnant, are pregnant or are post pregnancy. We are a private one-to-one pilates studio and will tailor packages to suit individual client's needs.

We want the colour scheme to be consistent to the website: www.deliaframptonpilates.com We want the overall theme to exude exclusivity as our target market is the affluent upper middle class in Kensington and Chelsea, London
Updates

Hi Guys,

Thank you for the questions!
A5 please, one sided, landscape. 
All the best,
Delia

To All the Designers,

Thank you so much for your submissions so far. I am extremely impressed with all of them! There are bits and pieces of a few designs that I think would look really nice if they were incorporated together. A few of
 the highlights are:
936979- I like this one, but please don't say, 'I am... (Delia Frampton) please just put, 'Delia with Soraya 5 months'
934981- I really like the layout but not the color scheme on this one. Please put the web address as: www.deliaframptonpilates.com
928472- This is my favorite design but the wording isn't quite right. 
927155-I like the layout and wording of this one.
931394- I like how, 'The Baby you dreamed of the body you deserve' is written. Please try and incorporate!
927947- I love how the website and studio logo is done. Please try and incorporate!
Thank you so much for all of your hard work and I look forward to seeing more of your submissions..
All the best,
Delia

Reason: Hi! I am still waiting for the updated versions of the advert since my last comments... please email me if you have any questions... Thank you so much and looking forward to seeing the submissions soon... Delia

Industry/Entity Type

Tailor

Requirements
Must have
• Incorporate the supplied photo (you can photoshop/alter the image as you see fit)

The picture is the studio owner with her daughter. Caption should read 'Delia with daughter Soraya, 5 months'

The design layout needs to work as both a flyer and as an advertisement in a magazine.

Needs to have website address, phone number (0207 555 0143), slogan 'The baby you dreamed of.....the body you deserve' & 'Whether you are pre or post pregnancy our team tailors programs for all stages'

You are free to suggest your take on how it looks, reads, design layout etc. Artistic freedom granted!
Nice to have
• Please refer to the attached recent press release by my PR agent. Please use any copy you feel necessary.

```html
<!DOCTYPE html>
<html lang="en">
<head>
<meta charset="utf-8">
<title>Delia Frampton Private Pilates Studio – Flyer</title>
<link rel="stylesheet" href="https://fonts.googleapis.com/css2?family=Inter:wght@300;400;600;700&display=swap">
<style>
  :root {
    --page: #ffffff;
    --wall-sun: #faf7f2;
    --wall-light: #ece5dc;
    --wall-mid: #d9cfc3;
    --wall-shade: #bdb2a5;
    --frond-shade: #8a9a6e;
    --leaf-light: #c4e46a;
    --leaf-mid: #6fb52c;
    --leaf-dark: #2f7a1c;
    --slogan-soft: #5f7fa8;
    --slogan-strong: #1d4fc4;
    --brand: #7a2fd0;
    --brand-soft: #a070dc;
    --ink-light: #ffffff;
    --caption: #3b3a38;
    --flare: #cfe6ff;
  }
  html, body {
    margin: 0;
    width: 1200px;
    height: 816px;
    overflow: hidden;
    background: var(--page);
  }
  .flyer {
    position: relative;
    width: 1200px;
    height: 816px;
    overflow: hidden;
    font-family: "Inter", Arial, sans-serif;
  }
  .flyer__photo {
    position: absolute;
    inset: 0;
    background:
      radial-gradient(ellipse 260px 200px at 1010px 90px, rgba(138,154,110,0.55) 0%, rgba(138,154,110,0.2) 55%, transparent 100%),
      radial-gradient(ellipse 420px 260px at 640px 120px, rgba(255,255,255,0.9) 0%, rgba(255,255,255,0) 100%),
      radial-gradient(ellipse 340px 420px at 1180px 560px, rgba(160,148,134,0.55) 0%, transparent 100%),
      linear-gradient(165deg, var(--wall-sun) 0%, var(--wall-light) 35%, var(--wall-mid) 70%, var(--wall-shade) 100%);
  }
  .flyer__leaf {
    position: absolute;
    inset: 0;
    width: 1200px;
    height: 816px;
  }
  .flyer__copy {
    position: absolute;
    left: 60px;
    top: 150px;
    width: 540px;
    text-align: right;
  }
  .slogan {
    margin: 0;
    text-transform: uppercase;
    line-height: 1;
  }
  .slogan__soft {
    display: block;
    font-weight: 300;
    color: var(--slogan-soft);
  }
  .slogan__strong {
    display: block;
    font-weight: 700;
    color: var(--slogan-strong);
  }
  .slogan--body .slogan__soft { font-size: 50px; }
  .slogan--body .slogan__strong { font-size: 58px; margin-top: 4px; }
  .slogan--baby { margin-top: 24px; }
  .slogan--baby .slogan__soft { font-size: 28px; }
  .slogan--baby .slogan__strong { font-size: 34px; margin-top: 2px; }
  .flare {
    display: block;
    height: 3px;
    margin: 14px 0 0 40px;
    background: linear-gradient(90deg, transparent, var(--flare) 60%, #ffffff 80%, transparent);
  }
  .brand { margin-top: 26px; }
  .brand__name {
    margin: 0;
    font-size: 44px;
    font-weight: 400;
    text-transform: uppercase;
    color: var(--brand);
    line-height: 1;
  }
  .brand__tagline {
    margin: 6px 0 0;
    font-size: 32px;
    font-weight: 300;
    color: var(--brand-soft);
  }
  .pitch {
    margin: 30px 0 0;
    font-size: 24px;
    font-weight: 400;
    line-height: 1.2;
    color: var(--ink-light);
  }
  .contact {
    margin: 28px 0 0;
    font-size: 19px;
    line-height: 1.3;
    color: var(--ink-light);
  }
  .caption {
    position: absolute;
    left: 700px;
    top: 740px;
    margin: 0;
    font-size: 14px;
    line-height: 1.2;
    text-align: center;
    color: var(--caption);
  }
</style>
</head>
<body>
<main class="flyer">
  <div class="flyer__photo" role="img" aria-label="Photograph of Delia in a sun hat and blue bikini holding her baby daughter against a sunlit wall with a palm frond"></div>

  <svg class="flyer__leaf" viewBox="0 0 1200 816" role="img" aria-label="Close-up of a green palm leaf filling a large circular panel">
    <defs>
      <linearGradient id="leafTone" x1="0" y1="0" x2="1" y2="1">
        <stop offset="0" stop-color="var(--leaf-light)"/>
        <stop offset="0.55" stop-color="var(--leaf-mid)"/>
        <stop offset="1" stop-color="var(--leaf-dark)"/>
      </linearGradient>
    </defs>
    <ellipse cx="80" cy="420" rx="600" ry="600" fill="url(#leafTone)"/>
  </svg>

  <section class="flyer__copy">
    <h1 class="slogan slogan--body">
      <span class="slogan__soft">“The Body</span>
      <span class="slogan__strong">You Deserve.”</span>
    </h1>
    <span class="flare"></span>
    <h2 class="slogan slogan--baby">
      <span class="slogan__soft">“The Baby</span>
      <span class="slogan__strong">You Dreamed Of..</span>
    </h2>

    <div class="brand">
      <p class="brand__name">Delia Frampton</p>
      <p class="brand__tagline">Private Pilates Studio</p>
    </div>

    <p class="pitch">“Whether you are pre or post<br>pregnancy our team tailors<br>programs for all stages.”</p>

    <p class="contact">Call us: 0207 555 0143<br>www.deliaframptonpilates.com</p>
  </section>

  <p class="caption">Delia with daughter Soraya,<br>5 months.</p>
</main>
</body>
</html>
```